New Business Card Design Project

Make a kick ass business card for The Otter Tea Mug, using the designs. I also might like the 2nd place design logo on the back? Maybe all black with that? Not sure. Also, I'm cool with it being on metal, plastic, glass? or whatever for the business card. Maybe shaped like a shark? Let me know what else you need? Would like designs in the next day or so. Thank you.
Target Market(s)
Anyone that is cool
Contact Information for Business Card
Name: Dorian Fenwick
Phone: 317.594.8126
inventor/creator/entrepreneur/owner
www.theottertyeamug.example
social media links
https://www.facebook.com/theottertyeamug
https://twitter.com/otter_brew
https://www.instagram.com/theottertyeamug/
I'll get the Pinterest one soon
Colors
Designer to choose colors to be used in the design.
Requirements
Must have
- The Otter Tea Mug
- www.theottertyeamug.example
- social media tags?
- My logos and picture/photo of wine glass
Nice to have
- Maybe shaped like a wine glass or shark
- I'll let you decide but my same colors from my website would be nice

```html
<!DOCTYPE html>
<html lang="en">
<head>
<meta charset="utf-8">
<title>The Otter Tea Mug — Business Card</title>
<link rel="stylesheet" href="https://fonts.googleapis.com/css2?family=Josefin+Sans:wght@300;400&family=Questrial&display=swap">
<style>
  :root {
    --page: #e9e8e5;
    --card-top: #3b3132;
    --card-mid: #1d1718;
    --card-bottom: #0c0a0a;
    --ink: #f4f1ef;
    --ink-soft: #d9d4d2;
    --glass-light: #6b6466;
    --glass-dark: #151112;
  }
  * { box-sizing: border-box; margin: 0; padding: 0; }
  html, body {
    width: 1013px;
    height: 1200px;
    overflow: hidden;
    background: var(--page);
  }
  .sheet {
    position: relative;
    width: 1013px;
    height: 1200px;
  }
  .card {
    position: absolute;
    left: 106px;
    width: 800px;
    color: var(--ink);
    border-radius: 16px;
    background: linear-gradient(180deg, var(--card-top) 0%, var(--card-mid) 40%, var(--card-bottom) 100%);
    overflow: hidden;
  }
  .card--front { top: 134px; height: 382px; }
  .card--back { top: 680px; height: 383px; }

  /* Front */
  .holder-name {
    position: absolute;
    left: 22px;
    top: 42px;
    font-family: "Josefin Sans", sans-serif;
    font-weight: 300;
    font-size: 46px;
    line-height: 1;
    padding-right: 6px;
    padding-bottom: 4px;
    border-bottom: 2px solid var(--ink-soft);
  }
  .holder-role {
    position: absolute;
    left: 24px;
    top: 104px;
    font-family: "Josefin Sans", sans-serif;
    font-weight: 300;
    font-size: 23px;
    letter-spacing: 4px;
  }
  .phone {
    position: absolute;
    left: 24px;
    top: 154px;
    display: flex;
    align-items: center;
    gap: 10px;
    font-family: "Questrial", sans-serif;
    font-size: 21px;
    letter-spacing: 2.5px;
  }
  .phone-icon { width: 20px; height: 20px; }
  .social-list {
    position: absolute;
    left: 24px;
    top: 278px;
    list-style: none;
    font-family: "Questrial", sans-serif;
    font-size: 15px;
    letter-spacing: 1.5px;
  }
  .social-list li {
    display: flex;
    align-items: center;
    gap: 9px;
    height: 28.5px;
  }
  .social-mark {
    width: 17px;
    height: 17px;
    border-radius: 3px;
    background: var(--ink);
  }
  .front-site {
    position: absolute;
    right: 20px;
    top: 358px;
    font-family: "Questrial", sans-serif;
    font-size: 15px;
    letter-spacing: 3px;
  }
  .glass-photo {
    position: absolute;
    left: 508px;
    top: 26px;
    width: 276px;
    height: 320px;
    border-radius: 40% 40% 46% 46% / 30% 30% 62% 62%;
    background: radial-gradient(ellipse at 50% 45%, var(--glass-light) 0%, #3a3334 45%, var(--glass-dark) 80%);
    opacity: 0.75;
  }

  /* Back */
  .brand-mark {
    position: absolute;
    left: 282px;
    top: 82px;
    width: 236px;
    height: 80px;
    border-radius: 50% 30% 40% 50% / 50% 50% 50% 50%;
    background: linear-gradient(90deg, #8f8a8a, #e4e1df 45%, #8f8a8a);
    opacity: 0.8;
  }
  .brand-name {
    position: absolute;
    left: 0;
    right: 0;
    top: 189px;
    text-align: center;
    font-family: "Questrial", sans-serif;
    font-weight: 400;
    font-size: 49px;
    line-height: 1.2;
    letter-spacing: 0.5px;
  }
  .back-site {
    position: absolute;
    left: 0;
    right: 0;
    top: 343px;
    text-align: center;
    font-family: "Questrial", sans-serif;
    font-size: 21px;
    letter-spacing: 5px;
  }
</style>
</head>
<body>
<main class="sheet">

  <section class="card card--front" aria-label="Business card front">
    <h1 class="holder-name">Dorian Fenwick</h1>
    <p class="holder-role">Owner</p>

    <p class="phone">
      <svg class="phone-icon" viewBox="0 0 24 24" aria-hidden="true">
        <path fill="currentColor" d="M6.6 10.8c1.4 2.8 3.8 5.1 6.6 6.6l2.2-2.2c.3-.3.7-.4 1-.2 1.1.4 2.3.6 3.6.6.6 0 1 .4 1 1V20c0 .6-.4 1-1 1C10.6 21 3 13.4 3 4c0-.6.4-1 1-1h3.5c.6 0 1 .4 1 1 0 1.3.2 2.5.6 3.6.1.3 0 .7-.2 1l-2.3 2.2z"/>
      </svg>
      <span>317 594 8126</span>
    </p>

    <ul class="social-list">
      <li><span class="social-mark" aria-hidden="true"></span><span>@theottertyeamug</span></li>
      <li><span class="social-mark" aria-hidden="true"></span><span>otter_brew</span></li>
      <li><span class="social-mark" aria-hidden="true"></span><span>theottertyeamug</span></li>
    </ul>

    <div class="glass-photo" role="img" aria-label="Photo of the product: a clear glass with a figure standing inside it"></div>

    <p class="front-site">www.theottertyeamug.example</p>
  </section>

  <section class="card card--back" aria-label="Business card back">
    <div class="brand-mark" role="img" aria-label="Brand logo mark"></div>
    <h2 class="brand-name">OtterTeaMug</h2>
    <p class="back-site">www.theottertyeamug.example</p>
  </section>

</main>
</body>
</html>
```